Brochure and Flyer template, Aluminium Facade company
Verdantis Structural Concepts pty Ltd
We are looking for a cutting edge Brochure and Flyer template that we can change text and pictures for different marketing products and services we provide to different target markets and audiences. We like a mixture of A4 size but also like the A5 size so please feel free to be creative.
Construction
Corporate, Building Companies, Architects, Home owners.
We are needing the Brochure template to cater for multiple product pictures and descriptions in either A4 or A5 format (please be creative) and the flier template is more aimed to focus on 1 or 2 individual products.
1 of 2 files of Past project photos for your use if you like
Our Logo
Our Logo Different Format
Our Company Profile (old and out dated for reference only!)
2 of 2 files of Past project photos for your use if you like
Past Projects for information on our company
SOME of our standard Products FOR YOUR INFORMATION ONLY
Havenor opening roof System Photos to go with the operable section Please make sure the Havenor logo is used
Our Products and Services description
Havenor opening Roof information
More Havenor opening roof pics and data. May be of use

```html
<!DOCTYPE html>
<html lang="en">
<head>
<meta charset="utf-8">
<title>Verdantis Structural Concepts – Brochure Cover</title>
<link href="https://fonts.googleapis.com/css2?family=Cinzel:wght@700&family=Roboto+Condensed:ital,wght@0,400;0,700;1,700&display=swap" rel="stylesheet">
<style>
  :root {
    --backdrop: #a9aaa9;
    --paper: #f7f8f6;
    --green: #2f8a3f;
    --green-dark: #1f6a2d;
    --green-light: #4ea85a;
    --ink-grey: #6b6f6c;
    --white: #ffffff;
  }
  * { margin: 0; padding: 0; box-sizing: border-box; }
  html, body {
    width: 1200px; height: 799px; overflow: hidden;
    background: var(--backdrop);
  }
  .canvas {
    position: relative; width: 1200px; height: 799px;
    background: radial-gradient(ellipse at 50% 40%, #b9bab9 0%, var(--backdrop) 70%);
  }
  .cover {
    position: absolute; left: 335px; top: 24px;
    width: 530px; height: 750px;
    background: var(--paper);
    box-shadow: 0 12px 30px rgba(0,0,0,0.25);
    overflow: hidden;
  }
  .cover__top-band {
    position: absolute; left: 0; top: 0; width: 100%; height: 42px;
    background: linear-gradient(180deg, var(--green-light), var(--green));
  }
  .cover__title {
    position: absolute; left: 0; top: 64px; width: 100%;
    text-align: center;
    font-family: "Cinzel", serif; font-weight: 700;
    font-size: 66px; line-height: 1; color: var(--green);
    letter-spacing: 1px;
  }
  .cover__subtitle {
    position: absolute; left: 0; top: 136px; width: 100%;
    text-align: center;
    font-family: "Roboto Condensed", sans-serif; font-weight: 700; font-style: italic;
    font-size: 21px; letter-spacing: 1.5px; color: var(--green-dark);
  }
  .cover__tagline {
    position: absolute; left: 0; top: 176px; width: 100%;
    text-align: center;
    font-family: "Roboto Condensed", sans-serif; font-weight: 400;
    font-size: 14px; letter-spacing: 2px; color: var(--ink-grey);
  }
  .cover__feature {
    position: absolute; left: 0; top: 212px; width: 100%; height: 360px;
    background: var(--green);
    padding: 10px 0 10px 24px;
  }
  .cover__photo {
    width: 100%; height: 100%;
    background: linear-gradient(90deg, #4f8fa8 0%, #6aa6bb 22%, #9a5a5e 40%, #7d7f86 58%, #8e9a78 76%, #7fa24f 100%);
  }
  .cover__link-band {
    position: absolute; left: 0; top: 572px; width: 100%; height: 56px;
    background: var(--green);
  }
  .cover__url {
    position: absolute; right: 22px; top: 12px;
    padding: 6px 18px;
    border: 2px solid var(--white); border-radius: 20px;
    background: var(--green-light);
    font-family: "Roboto Condensed", sans-serif; font-weight: 400;
    font-size: 15px; color: var(--white); letter-spacing: 0.5px;
  }
  .brand {
    position: absolute; left: 30px; top: 656px;
    display: flex; align-items: center; gap: 12px;
  }
  .brand__mark {
    width: 50px; height: 50px; border-radius: 50%;
    background: var(--green);
  }
  .brand__name {
    font-family: "Cinzel", serif; font-weight: 700;
    font-size: 32px; line-height: 1; color: var(--green);
  }
  .brand__descriptor {
    font-family: "Roboto Condensed", sans-serif; font-weight: 700;
    font-size: 11px; letter-spacing: 1px; color: var(--green);
    margin-top: 4px;
  }
</style>
</head>
<body>
<div class="canvas">
  <article class="cover">
    <div class="cover__top-band"></div>
    <h1 class="cover__title">VERDANTIS</h1>
    <p class="cover__subtitle">STRUCTURAL CONCEPTS</p>
    <p class="cover__tagline">INNOVATION • DESIGN • SUSTAINABILITY</p>
    <div class="cover__feature">
      <div class="cover__photo" role="img" aria-label="Photo of a coloured aluminium louvre facade in blue, red, grey and green tones"></div>
    </div>
    <div class="cover__link-band">
      <span class="cover__url">verdantisstructural.com.au</span>
    </div>
    <div class="brand">
      <div class="brand__mark"></div>
      <div>
        <div class="brand__name">VERDANTIS</div>
        <div class="brand__descriptor">STRUCTURAL CONCEPTS</div>
      </div>
    </div>
  </article>
</div>
</body>
</html>
```